Brimvane.com fiber optic internet website redesign

We need a new website design for our fiber optic internet company that provides internet, phone, and tv services. It should use the text "Marrowfen fiber optics", and "I beamed up with Marrowfen". The design should use the color blue and the attached logo.
We are a 30 year old internet company who started as a dial up internet provider in our basement. Today we design, build, and maintain our own fiber optic internet network to provide service to residential, business, educational, healthcare, and governmental customers

```html
<!DOCTYPE html>
<html lang="en">
<head>
<meta charset="utf-8">
<title>Marrowfen Fiber Optics</title>
<link href="https://fonts.googleapis.com/css2?family=Rubik:wght@400;500;600;700&family=Heebo:wght@400;500;700&display=swap" rel="stylesheet">
<style>
:root{
  --blue:#1b52d6;
  --blue-dark:#1543b0;
  --navy:#13224b;
  --navy-deep:#0d1a3d;
  --ink:#1b1f2b;
  --muted:#7c8293;
  --red:#e0232b;
  --line:#e3e6ee;
  --soft:#f4f6fa;
  --green:#23b47e;
}
*{margin:0;padding:0;box-sizing:border-box}
html,body{width:1200px;height:5393px;overflow:hidden}
body{font-family:"Heebo",sans-serif;color:var(--ink);background:#fff;position:relative}
h1,h2,h3,h4{font-family:"Rubik",sans-serif}
section,header,footer{position:relative;width:1200px}
.abs{position:absolute}
.btn{position:absolute;display:flex;align-items:center;justify-content:center;gap:6px;background:var(--blue);color:#fff;font:600 11px "Rubik",sans-serif;border-radius:22px;letter-spacing:.3px;text-transform:uppercase}
.btn svg{width:10px;height:10px}
.photo{position:absolute}

/* header */
.site-header{height:113px;background:#fff;box-shadow:0 2px 8px rgba(0,0,0,.05)}
.brand-panel{position:absolute;left:0;top:0;width:285px;height:113px;background:var(--blue);clip-path:polygon(0 0,100% 0,82% 100%,0 100%)}
.brand{position:absolute;left:22px;top:30px;color:#fff;display:flex;align-items:center;gap:10px}
.brand-dot{width:38px;height:38px;border-radius:50%;border:3px solid #fff}
.brand-name{font:700 34px "Rubik",sans-serif;line-height:1}
.brand-sub{font:400 12px "Rubik",sans-serif;line-height:1.4}
.topbar{position:absolute;top:12px;left:285px;right:0;height:22px;font-size:11px;color:#4a5060;display:flex;align-items:center}
.topbar span{position:absolute;display:flex;align-items:center;gap:6px;white-space:nowrap}
.topbar svg{width:12px;height:12px}
.socials{position:absolute;display:flex;gap:10px}
.socials i{width:10px;height:10px;border-radius:50%;background:#5a6070;display:block}
.nav{position:absolute;top:68px;font:500 12px "Rubik",sans-serif;color:var(--ink);text-transform:uppercase}
.service-call{position:absolute;left:878px;top:58px;display:flex;gap:10px;align-items:center}
.service-call small{display:block;font-size:11px;color:var(--muted)}
.service-call b{font:600 14px "Rubik",sans-serif;color:var(--red)}

/* hero */
.hero{height:603px;background:linear-gradient(120deg,#1a2b5c 0%,#27407a 45%,#1c2f64 100%)}
.hero-title{position:absolute;left:96px;top:130px;color:#fff;font:700 62px/1.15 "Rubik",sans-serif;text-transform:uppercase}
.hero-list{position:absolute;left:96px;top:296px;list-style:none;color:#fff;font:600 11px "Rubik",sans-serif}
.hero-list li{display:flex;gap:12px;align-items:center;height:35px}
.hero-list svg{width:14px;height:14px}
.plan-card{position:absolute;top:547px;width:319px;height:200px;color:#fff;padding:24px 32px}
.plan-card h3{font:500 26px "Rubik",sans-serif}
.plan-card .sub{font-size:13px;margin-top:6px}
.plan-card .price{display:flex;align-items:flex-start;margin-top:22px}
.plan-card .price sup{font-size:13px;margin-top:6px}
.plan-card .price strong{font:600 48px/1 "Rubik",sans-serif}
.plan-card .price em{font:600 11px/1.25 "Rubik",sans-serif;font-style:normal;margin:14px 0 0 8px;text-transform:uppercase}
.plan-card .tab{position:absolute;left:32px;bottom:-2px;background:#fff;color:var(--ink);font-size:11px;padding:7px 18px 12px;border-radius:14px 14px 0 0;display:flex;gap:6px;align-items:center}
.plan-card .tab svg{width:9px;height:9px}
.card-blue{background:var(--blue)}
.card-navy{background:var(--navy-deep)}

/* experience */
.experience{height:771px}
.section-title{font:500 38px/1.2 "Rubik",sans-serif;color:var(--ink)}
.body-copy{font-size:12px;line-height:1.85;color:var(--muted)}
.stat b{display:block;font:600 22px "Rubik",sans-serif;color:var(--red)}
.stat span{font:500 12px "Rubik",sans-serif}

/* why */
.why{height:475px;background:linear-gradient(180deg,#1b2b5b,#15244f)}
.why h2{position:absolute;top:92px;width:100%;text-align:center;color:#fff;font:500 36px "Rubik",sans-serif}
.feature{position:absolute;top:180px;width:240px;text-align:center;color:#fff}
.feature svg{width:44px;height:44px}
.feature h4{font:500 16px "Rubik",sans-serif;margin-top:26px}
.feature p{font-size:11.5px;line-height:1.85;color:#aeb6cc;margin-top:18px}
.feature a{display:inline-flex;gap:6px;align-items:center;font:600 10px "Rubik",sans-serif;margin-top:18px;text-transform:uppercase}
.feature a svg{width:9px;height:9px}

/* special */
.special{height:691px}
.badge{position:absolute;left:172px;top:83px;width:100px;height:100px;border-radius:50%;background:#141414;color:#fff;font:600 12px/1.4 "Rubik",sans-serif;display:flex;align-items:center;justify-content:center;text-align:center;text-transform:uppercase}

/* cta */
.cta{height:419px;background:linear-gradient(100deg,#2c3e6e,#3b507f 50%,#2d3f6c)}
.cta h2{position:absolute;top:118px;width:100%;text-align:center;color:#fff;font:500 36px/1.3 "Rubik",sans-serif}
.btn-outline{background:transparent;border:1.5px solid #fff}

/* plans */
.plans{height:688px}
.plans h2{position:absolute;top:75px;width:100%;text-align:center}
.tier{position:absolute;top:228px;width:318px;height:370px;border:1px solid var(--line);text-align:center}
.tier h3{font:500 18px "Rubik",sans-serif;margin-top:34px}
.tier .icons{margin-top:18px;display:flex;justify-content:center;gap:6px;align-items:center;color:var(--red);font-weight:700}
.tier .icons svg{width:22px;height:22px}
.tier ul{list-style:none;text-align:left;margin:24px 0 0 38px;font-size:12px;color:#4a5060}
.tier li{display:flex;gap:10px;align-items:center;height:30px}
.tier li i{width:10px;height:10px;border-radius:50%;background:var(--green);display:block}
.tier .from{margin-top:16px;font-size:12px;color:#4a5060}
.tier .from strong{font:500 30px "Rubik",sans-serif;color:var(--ink)}

/* faq */
.faq{height:684px}
.accordion{position:absolute;left:96px;top:218px;width:492px;border:1px solid var(--line)}
.acc-item{border-bottom:1px solid var(--line);padding:14px 20px;font:500 12px "Rubik",sans-serif;display:flex;gap:22px;align-items:center}
.acc-item:last-child{border-bottom:none}
.acc-answer{padding:0 20px 18px 20px;font-size:11.5px;line-height:1.85;color:var(--muted)}

/* tv */
.tv{height:561px;background:linear-gradient(160deg,#1c2b55,#141f42)}
.offer-seal{position:absolute;left:526px;top:86px;width:144px;height:144px;border-radius:50%;background:var(--red);color:#fff;text-align:center;display:flex;flex-direction:column;justify-content:center;font:600 11px "Rubik",sans-serif;text-transform:uppercase;z-index:2}
.offer-seal strong{font:600 40px/1.05 "Rubik",sans-serif}

/* footer */
.site-footer{height:303px;background:var(--soft)}
.foot-col{position:absolute;top:0;height:303px}
.foot-col h4{position:absolute;top:78px;font:500 13px "Rubik",sans-serif;text-transform:uppercase;white-space:nowrap}
.foot-col ul{position:absolute;top:118px;list-style:none;font-size:12px;color:#5a6070;white-space:nowrap}
.foot-col li{height:29px}
.divider{position:absolute;top:0;width:1px;height:303px;background:var(--line)}
.bottom-bar{height:85px;background:var(--navy)}
</style>
</head>
<body>

<header class="site-header">
  <div class="brand-panel"></div>
  <div class="brand">
    <span class="brand-dot"></span>
    <div><div class="brand-name">BRIMVANE</div><div class="brand-sub">Marrowfen Fiber Optics</div></div>
  </div>
  <div class="topbar">
    <span style="left:0"><svg viewBox="0 0 12 12"><path d="M6 1a3.5 3.5 0 0 0-3.5 3.5C2.5 7.5 6 11 6 11s3.5-3.5 3.5-6.5A3.5 3.5 0 0 0 6 1z" fill="none" stroke="#e0232b" stroke-width="1.2"/></svg>88 Lantern Row, Elmsford, PA 16000</span>
    <span style="left:228px"><svg viewBox="0 0 12 12"><rect x="1" y="2.5" width="10" height="7" fill="none" stroke="#e0232b" stroke-width="1.2"/><path d="M1 3l5 4 5-4" fill="none" stroke="#e0232b" stroke-width="1.2"/></svg>sales@marrowfen-fiber.net</span>
    <span style="left:388px"><svg viewBox="0 0 12 12"><circle cx="6" cy="6" r="4.8" fill="none" stroke="#e0232b" stroke-width="1.2"/><path d="M6 3.5V6l1.8 1.2" fill="none" stroke="#e0232b" stroke-width="1.2"/></svg>Opening Time : 10 AM - 10 PM</span>
    <span style="left:675px"><svg viewBox="0 0 12 12"><circle cx="6" cy="4" r="2.5" fill="none" stroke="#e0232b" stroke-width="1.2"/><path d="M1.5 11c.5-2.5 2.3-3.8 4.5-3.8s4 1.3 4.5 3.8" fill="none" stroke="#e0232b" stroke-width="1.2"/></svg>Login / Register</span>
    <div class="socials" style="left:812px;top:6px"><i></i><i></i><i></i><i></i></div>
  </div>
  <nav>
    <span class="nav" style="left:285px">Home</span>
    <span class="nav" style="left:350px">About</span>
    <span class="nav" style="left:420px">Residential</span>
    <span class="nav" style="left:527px">Business</span>
    <span class="nav" style="left:616px">Telecom</span>
    <span class="nav" style="left:702px">Services</span>
  </nav>
  <div class="service-call">
    <svg width="20" height="32" viewBox="0 0 20 32"><rect x="2" y="1" width="16" height="30" rx="3" fill="none" stroke="#e0232b" stroke-width="2"/><circle cx="10" cy="26" r="1.5" fill="#e0232b"/></svg>
    <div><small>Customer Service:</small><b>1-888-555-0142</b></div>
  </div>
  <a class="btn" style="left:1062px;top:57px;width:126px;height:38px">Get a Quote <svg viewBox="0 0 10 10"><path d="M1 5h7M5 2l3 3-3 3" fill="none" stroke="#fff" stroke-width="1.4"/></svg></a>
</header>

<section class="hero">
  <div class="photo" role="img" aria-label="Night city skyline with glowing network lines connecting buildings" style="inset:0;background:linear-gradient(120deg,#1a2b5c 0%,#2a4584 50%,#1b2d60 100%)"></div>
  <h1 class="hero-title">I beamed up with<br>Marrowfen</h1>
  <ul class="hero-list">
    <li><svg viewBox="0 0 14 14"><rect x="1" y="1" width="12" height="12" fill="none" stroke="#fff" stroke-width="1.3"/><path d="M4 7l2.2 2.2L11 4" fill="none" stroke="#fff" stroke-width="1.4"/></svg>High Speed Bandwidth Connections</li>
    <li><svg viewBox="0 0 14 14"><rect x="1" y="1" width="12" height="12" fill="none" stroke="#fff" stroke-width="1.3"/><path d="M4 7l2.2 2.2L11 4" fill="none" stroke="#fff" stroke-width="1.4"/></svg>Any Device Connectivity</li>
    <li><svg viewBox="0 0 14 14"><rect x="1" y="1" width="12" height="12" fill="none" stroke="#fff" stroke-width="1.3"/><path d="M4 7l2.2 2.2L11 4" fill="none" stroke="#fff" stroke-width="1.4"/></svg>Streaming TV Box &amp; Satellite Live TV</li>
  </ul>
  <a class="btn" style="left:96px;top:427px;width:136px;height:42px">Contact Us <svg viewBox="0 0 10 10"><path d="M1 5h7M5 2l3 3-3 3" fill="none" stroke="#fff" stroke-width="1.4"/></svg></a>

  <article class="plan-card card-blue" style="left:96px">
    <h3>High Speed</h3><p class="sub">Internet Service</p>
    <div class="price"><sup>$</sup><strong>55</strong><em>From<br>/Month</em></div>
    <span class="tab">View Plans <svg viewBox="0 0 10 10"><path d="M1 5h7M5 2l3 3-3 3" fill="none" stroke="#1b1f2b" stroke-width="1.4"/></svg></span>
  </article>
  <article class="plan-card card-navy" style="left:440px">
    <h3>VoIP</h3><p class="sub">Phone Service</p>
    <div class="price"><sup>$</sup><strong>25</strong><em>From<br>/Month</em></div>
    <span class="tab">View Plans <svg viewBox="0 0 10 10"><path d="M1 5h7M5 2l3 3-3 3" fill="none" stroke="#1b1f2b" stroke-width="1.4"/></svg></span>
  </article>
  <article class="plan-card card-blue" style="left:783px">
    <h3>Phone &amp; Internet</h3><p class="sub">Packages</p>
    <div class="price"><sup>$</sup><strong>80</strong><em>From<br>/Month</em></div>
    <span class="tab">View Plans <svg viewBox="0 0 10 10"><path d="M1 5h7M5 2l3 3-3 3" fill="none" stroke="#1b1f2b" stroke-width="1.4"/></svg></span>
  </article>
</section>

<section class="experience">
  <div class="photo" role="img" aria-label="Family relaxing at home with laptop, TV streaming box and router" style="left:126px;top:272px;width:439px;height:244px;background:linear-gradient(135deg,#e9e4dc,#b9b2a6)"></div>
  <div class="photo" role="img" aria-label="Router and streaming device" style="left:96px;top:430px;width:170px;height:226px;background:linear-gradient(160deg,#5a5d66,#1d1e22)"></div>
  <div class="photo" role="img" aria-label="Living room with wall-mounted TV" style="left:364px;top:500px;width:201px;height:140px;background:linear-gradient(135deg,#c9cbcf,#6f7580)"></div>
  <h2 class="section-title abs" style="left:611px;top:256px">Experience The<br>Difference</h2>
  <p class="body-copy abs" style="left:611px;top:388px;width:495px">Marrowfen outperforms other local Internet and phone service providers by delivering Internet and phone service over the newest, most reliable communications network – Fiber Optics! Utilizing our own fiber optic network, we can bring you internet speeds that far surpass traditional DSL or Cable services. Internet service that is consistent and reliable, combined with superior phone voice quality, makes Marrowfen Fiber Optic the perfect choice for home and business.</p>
  <div class="stat abs" style="left:611px;top:544px"><b>4k</b><span>Ultra HD Quality</span></div>
  <div class="stat abs" style="left:783px;top:544px"><b>90+</b><span>Online TV Channels</span></div>
  <div class="stat abs" style="left:955px;top:544px"><b>350+</b><span>Mbps Speed Internet</span></div>
  <a class="btn" style="left:611px;top:636px;width:134px;height:40px">Try Us Now <svg viewBox="0 0 10 10"><path d="M1 5h7M5 2l3 3-3 3" fill="none" stroke="#fff" stroke-width="1.4"/></svg></a>
</section>

<section class="why">
  <h2>Why Choose Us</h2>
  <div class="feature" style="left:98px">
    <svg viewBox="0 0 44 44" fill="none" stroke="#2e63e0" stroke-width="2"><path d="M6 20L22 8l16 12"/><rect x="10" y="20" width="24" height="16"/><path d="M18 36v-8h8v8"/></svg>
    <h4>Local Support</h4><p>Sed ut perspiciatis unde omnis iste natus error sit voluptatem accusantium</p>
    <a>Read More <svg viewBox="0 0 10 10"><path d="M1 5h7M5 2l3 3-3 3" fill="none" stroke="#fff" stroke-width="1.4"/></svg></a>
  </div>
  <div class="feature" style="left:352px">
    <svg viewBox="0 0 44 44" fill="none" stroke="#2e63e0" stroke-width="2"><rect x="6" y="26" width="32" height="10" rx="2"/><path d="M14 26l4-16M30 26l-4-16M22 10v-4"/><circle cx="12" cy="31" r="1"/></svg>
    <h4>High Speed Internet</h4><p>Sed ut perspiciatis unde omnis iste natus error sit voluptatem accusantium</p>
    <a>Read More <svg viewBox="0 0 10 10"><path d="M1 5h7M5 2l3 3-3 3" fill="none" stroke="#fff" stroke-width="1.4"/></svg></a>
  </div>
  <div class="feature" style="left:606px">
    <svg viewBox="0 0 44 44" fill="none" stroke="#2e63e0" stroke-width="2"><path d="M10 14a16 16 0 0 0 20 20L10 14z"/><path d="M20 24l10-10M28 8a8 8 0 0 1 8 8M28 3a13 13 0 0 1 13 13"/><path d="M14 30l-4 8h16"/></svg>
    <h4>Fast &amp; Secure</h4><p>Sed ut perspiciatis unde omnis iste natus error sit voluptatem accusantium</p>
    <a>Read More <svg viewBox="0 0 10 10"><path d="M1 5h7M5 2l3 3-3 3" fill="none" stroke="#fff" stroke-width="1.4"/></svg></a>
  </div>
  <div class="feature" style="left:860px">
    <svg viewBox="0 0 44 44" fill="none" stroke="#2e63e0" stroke-width="2"><rect x="4" y="12" width="36" height="22" rx="2"/><circle cx="22" cy="23" r="6"/><path d="M22 19v8"/></svg>
    <h4>Affordable Prices</h4><p>Sed ut perspiciatis unde omnis iste natus error sit voluptatem accusantium</p>
    <a>Read More <svg viewBox="0 0 10 10"><path d="M1 5h7M5 2l3 3-3 3" fill="none" stroke="#fff" stroke-width="1.4"/></svg></a>
  </div>
</section>

<section class="special">
  <span class="abs" style="left:97px;top:163px;width:30px;height:30px;border-radius:50%;background:var(--blue)"></span>
  <div class="photo" role="img" aria-label="Two women smiling at a tablet under a large wifi symbol" style="left:134px;top:93px;width:431px;height:445px;background:linear-gradient(160deg,#f2f3f5 0%,#cfd4dc 55%,#8a8f99 100%)"></div>
  <div class="badge">Special<br>Offer</div>
  <h2 class="section-title abs" style="left:611px;top:201px">Get Broadband Network<br>At Very Cheap Price</h2>
  <p class="body-copy abs" style="left:611px;top:332px;width:480px">Marrowfen Fiber Optic service offers low cost, high quality, and extremely reliable Phone, TV and high-speed Internet access.</p>
  <a class="btn" style="left:611px;top:444px;width:141px;height:40px">Get Started <svg viewBox="0 0 10 10"><path d="M1 5h7M5 2l3 3-3 3" fill="none" stroke="#fff" stroke-width="1.4"/></svg></a>
</section>

<section class="cta">
  <div class="photo" role="img" aria-label="Couple relaxing on a sofa with a laptop" style="inset:0;background:linear-gradient(100deg,#2c3e6e,#44598a 50%,#2d3f6c)"></div>
  <h2>Need Fast &amp; Secure Broadband? Use<br>Marrowfen Fiber Optic.</h2>
  <a class="btn" style="left:418px;top:251px;width:157px;height:42px">View Our Plans <svg viewBox="0 0 10 10"><path d="M1 5h7M5 2l3 3-3 3" fill="none" stroke="#fff" stroke-width="1.4"/></svg></a>
  <span class="abs" style="left:591px;top:265px;color:#fff;font:600 11px Rubik,sans-serif">OR</span>
  <a class="btn btn-outline" style="left:623px;top:251px;width:159px;height:42px">1-888-555-0142 <svg viewBox="0 0 10 10"><path d="M1 5h7M5 2l3 3-3 3" fill="none" stroke="#fff" stroke-width="1.4"/></svg></a>
</section>

<section class="plans">
  <h2 class="section-title">Discover Our Best<br>Value Plans</h2>
  <div class="tier" style="left:96px">
    <h3>Residential Services</h3>
    <div class="icons"><svg viewBox="0 0 22 22" fill="none" stroke="#e0232b" stroke-width="1.5"><rect x="2" y="4" width="18" height="11"/><path d="M8 19h6M11 15v4"/></svg>+<svg viewBox="0 0 22 22" fill="none" stroke="#e0232b" stroke-width="1.5"><circle cx="11" cy="7" r="4"/><path d="M3 20c1-5 4-7 8-7s7 2 8 7z"/></svg></div>
    <ul><li><i></i>Internet Service</li><li><i></i>Phone Service</li><li><i></i>Video Service</li><li><i></i>Internet &amp; Phone Packages</li></ul>
    <p class="from">From <strong>$55</strong>/Month</p>
    <a class="btn" style="left:98px;top:306px;width:122px;height:38px">View Plans <svg viewBox="0 0 10 10"><path d="M1 5h7M5 2l3 3-3 3" fill="none" stroke="#fff" stroke-width="1.4"/></svg></a>
  </div>
  <div class="tier" style="left:440px">
    <h3>Business Services</h3>
    <div class="icons"><svg viewBox="0 0 22 22" fill="none" stroke="#e0232b" stroke-width="1.5"><rect x="2" y="4" width="18" height="11"/><path d="M8 19h6M11 15v4"/></svg>+<svg viewBox="0 0 22 22" fill="none" stroke="#e0232b" stroke-width="1.5"><circle cx="11" cy="7" r="4"/><path d="M3 20c1-5 4-7 8-7s7 2 8 7z"/></svg></div>
    <ul><li><i></i>SOHO Internet</li><li><i></i>Enterprise Internet</li><li><i></i>Phone Service</li><li><i></i>Hosted PBX</li></ul>
    <p class="from">From <strong>$55</strong>/Month</p>
    <a class="btn" style="left:98px;top:306px;width:122px;height:38px">View Plans <svg viewBox="0 0 10 10"><path d="M1 5h7M5 2l3 3-3 3" fill="none" stroke="#fff" stroke-width="1.4"/></svg></a>
  </div>
  <div class="tier" style="left:783px">
    <h3>Other Services</h3>
    <div class="icons"><svg viewBox="0 0 22 22" fill="none" stroke="#e0232b" stroke-width="1.5"><rect x="2" y="4" width="18" height="11"/><path d="M8 19h6M11 15v4"/></svg>+<svg viewBox="0 0 22 22" fill="none" stroke="#e0232b" stroke-width="1.5"><circle cx="11" cy="7" r="4"/><path d="M3 20c1-5 4-7 8-7s7 2 8 7z"/></svg></div>
    <ul><li><i></i>Managed Hosting</li><li><i></i>Virtual Hosting</li><li><i></i>Colocation</li><li><i></i>Hosted PBX</li></ul>
    <p class="from">From <strong>$55</strong>/Month</p>
    <a class="btn" style="left:98px;top:306px;width:122px;height:38px">View Plans <svg viewBox="0 0 10 10"><path d="M1 5h7M5 2l3 3-3 3" fill="none" stroke="#fff" stroke-width="1.4"/></svg></a>
  </div>
</section>

<section class="faq">
  <h2 class="section-title abs" style="left:92px;top:90px;font-size:40px">Frequently Asked<br>Questions</h2>
  <div class="accordion">
    <div class="acc-item" style="border-bottom:none"><span>+</span>Do I have to be an existing Northway Mobile customer?</div>
    <p class="acc-answer">Yes! You'll be able to use your Northway Mobile Home Internet to connect your computer, phone, and numerous other devices in your home simultaneously. People over time-we appreciate your patience! As soon as we're ready for you, we'll let you know</p>
    <div class="acc-item" style="border-top:1px solid var(--line)"><span>+</span>What is a commercial on-line service?</div>
    <div class="acc-item"><span>+</span>How much does the Northway Mobile Home Internet plan cost?</div>
    <div class="acc-item"><span>+</span>How can I get Internet for my business?</div>
    <div class="acc-item"><span>+</span>When do you expect to roll out more markets?</div>
  </div>
  <h3 class="abs" style="left:611px;top:224px;font:500 20px Rubik,sans-serif">We are everywhere</h3>
  <p class="body-copy abs" style="left:611px;top:262px;width:380px;font-size:11px">Home Internet customers that did not provide an email address for service notifications</p>
  <div class="photo" role="img" aria-label="Dotted world map with coloured location pins" style="left:611px;top:330px;width:490px;height:210px;background:radial-gradient(ellipse at center,#d8dbe2 0%,#eef0f4 60%,#fff 100%)"></div>
  <a class="btn" style="left:750px;top:528px;width:213px;height:42px;text-transform:none;background:var(--blue-dark)">Check Your Network Coverage</a>
</section>

<section class="tv">
  <h2 class="abs" style="left:96px;top:160px;color:#fff;font:500 40px/1.25 Rubik,sans-serif">Enjoy Sports Movies,<br>TV Shows &amp; More</h2>
  <p class="abs" style="left:96px;top:298px;width:420px;color:#d6dbe8;font-size:12px;line-height:1.8">If you are going to use a passage of Lorem Ipsum, you need to be sure there isn't anything hidden in the middle of text</p>
  <a class="btn" style="left:96px;top:376px;width:136px;height:42px">Try Us Free <svg viewBox="0 0 10 10"><path d="M1 5h7M5 2l3 3-3 3" fill="none" stroke="#fff" stroke-width="1.4"/></svg></a>
  <div class="offer-seal"><span>Only</span><strong>$89</strong><span>Monthly</span></div>
  <div class="photo" role="img" aria-label="TV screen showing a grid of streaming channel tiles next to a remote and stick" style="left:553px;top:110px;width:492px;height:325px;background:linear-gradient(135deg,#5b3fa0,#b0326a 50%,#2a2f55)"></div>
</section>

<footer class="site-footer">
  <div class="foot-col" style="left:145px">
    <svg class="abs" style="left:0;top:72px" width="38" height="38" viewBox="0 0 38 38" fill="none" stroke="#e0232b" stroke-width="2.5"><path d="M6 24v-6a13 13 0 0 1 26 0v6"/><rect x="4" y="22" width="7" height="10" rx="2" fill="#e0232b"/><rect x="27" y="22" width="7" height="10" rx="2" fill="#e0232b"/></svg>
    <div class="abs" style="left:50px;top:74px;white-space:nowrap"><div style="font-size:12px;color:#5a6070">Call us 24/7</div><div style="font:600 14px Rubik,sans-serif">1-888-555-0142</div></div>
    <div class="abs" style="left:0;top:138px;font:600 13px Rubik,sans-serif;white-space:nowrap">Contact info</div>
    <div class="abs" style="left:0;top:160px;font-size:11.5px;line-height:1.9;color:#5a6070;white-space:nowrap">Marrowfen Inc. 88 Lantern Row<br>Elmsford, PA 16000</div>
    <div class="socials abs" style="left:0;top:222px"><i style="width:20px;height:20px;background:#dfe3ec"></i><i style="width:20px;height:20px;background:#dfe3ec"></i><i style="width:20px;height:20px;background:#dfe3ec"></i><i style="width:20px;height:20px;background:#dfe3ec"></i></div>
  </div>
  <span class="divider" style="left:405px"></span>
  <div class="foot-col" style="left:456px"><h4>Services</h4><ul><li>Internet</li><li>Phone</li><li>Video</li><li>SOHO Internet</li><li>Managed Hosting</li></ul></div>
  <span class="divider" style="left:650px"></span>
  <div class="foot-col" style="left:698px"><h4>About Company</h4><ul><li>About Us</li><li>Contact Us</li><li>Faq</li><li>User</li><li>Support</li></ul></div>
  <span class="divider" style="left:890px"></span>
  <div class="foot-col" style="left:940px"><h4>Service Schedule</h4>
    <ul style="line-height:1.6"><li style="height:50px">Saturday – Sunday – Mon<br><b style="color:var(--ink);font-weight:500">8:30 AM – 10 PM</b></li><li style="height:50px">Tuesday – Wed – Thurs<br><b style="color:var(--ink);font-weight:500">9:30 AM – 12 PM</b></li><li>Friday : <span style="color:var(--red)">Closed</span></li></ul>
  </div>
</footer>

<div class="bottom-bar" style="position:relative;width:1200px">
  <div class="abs" style="left:100px;top:22px;display:flex;gap:10px;align-items:center;color:#fff">
    <span style="width:32px;height:32px;border-radius:50%;border:2.5px solid #fff;display:block"></span>
    <div><div style="font:700 24px/1 Rubik,sans-serif">BRIMVANE</div><div style="font-size:9px">Marrowfen Fiber Optics</div></div>
  </div>
  <p class="abs" style="right:96px;top:35px;color:#fff;font-size:12px">Copyright © 2025, All Rights Reserved.</p>
</div>

</body>
</html>
```